Business Card for Quillmark Ledger - A cannabis publication for executives.

I'd like some business cards for Quillmark Ledger. The logo is done (great job!) and I need a card design I will use with PRINTLY. I made it a short project to allow time for printing before an event. These will be standard sized cards (final artwork size 3.66" x 2.16" at 300dpi) with a final card size of 3.5" x 2.0". (See PRINTLY.com if you need more info.) I might try rounded corners but am not sure yet. I think the design will work okay with rounded.

Quillmark Ledger will be a bi-weekly publication for the cannabis industry. It is targeted to investors and industry executives, not consumers or pot smokers. So our market is more B2B. However I am open to creativity and making the card something people remark on.

My contact for card:

Dana Merrow
Founder/CEO
dana@quillmarkledger.example

2740 Harlow Avenue
Boston MA 02135
(617)555-0194

Target Market(s)

Executives, Industry people and investors in the Cannabis sector.

Contact Information for Business Card

PRINTLY does do double sided and the second side can be the same or different images. Only one side is required but use of the second side would be a bonus.

Font styles to use
Serif
Sans Serif
Decorative

Colors

Designer to choose colors to be used in the design.

Requirements
Must have
• Logo, contact info
Nice to have
• Style and design to make the card stand out in a crowd.

```html
<!DOCTYPE html>
<html lang="en">
<head>
<meta charset="utf-8">
<title>Quillmark Ledger Business Cards</title>
<link href="https://fonts.googleapis.com/css2?family=Lato:wght@400;700;900&display=swap" rel="stylesheet">
<style>
  :root {
    --brand-blue: #2a5c9c;
    --brand-green: #6aa22a;
    --ink: #1d1d1d;
    --paper: #f7f7f7;
    --backdrop: #ececec;
  }
  html, body {
    margin: 0;
    padding: 0;
    width: 1200px;
    height: 586px;
    overflow: hidden;
    background: var(--backdrop);
    font-family: "Lato", Arial, sans-serif;
  }
  .stage {
    position: relative;
    width: 1200px;
    height: 586px;
  }
  .card {
    position: absolute;
    top: 143px;
    width: 501px;
    height: 300px;
    overflow: hidden;
  }
  .card--front {
    left: 61px;
    background: var(--brand-blue);
    color: #fff;
  }
  .card--back {
    left: 619px;
    background: var(--paper);
    color: var(--ink);
  }
  .wordmark {
    position: absolute;
    display: flex;
    align-items: center;
    gap: 12px;
    font-weight: 700;
    white-space: nowrap;
  }
  .wordmark__dot {
    border-radius: 50%;
    flex: none;
  }
  .card--front .wordmark {
    left: 0;
    right: 0;
    top: 113px;
    justify-content: center;
    font-size: 36px;
    color: #fff;
  }
  .card--front .wordmark__dot {
    width: 44px;
    height: 44px;
    border: 5px solid #fff;
    box-sizing: border-box;
  }
  .website {
    position: absolute;
    left: 0;
    right: 0;
    top: 262px;
    text-align: center;
    font-size: 10px;
    font-weight: 700;
    letter-spacing: 3px;
  }
  .card--back .wordmark {
    right: 34px;
    top: 36px;
    font-size: 25px;
    color: var(--brand-blue);
    gap: 10px;
  }
  .card--back .wordmark__dot {
    width: 34px;
    height: 34px;
    background: var(--brand-green);
  }
  .contact {
    position: absolute;
    left: 34px;
    top: 133px;
  }
  .contact__name {
    margin: 0;
    font-size: 17px;
    font-weight: 900;
    color: var(--brand-green);
  }
  .contact__title {
    margin: 3px 0 0;
    font-size: 11px;
  }
  .contact__list {
    list-style: none;
    margin: 20px 0 0;
    padding: 0;
    font-size: 12px;
  }
  .contact__item {
    display: flex;
    align-items: center;
    gap: 8px;
    height: 25px;
  }
  .contact__icon {
    width: 17px;
    height: 17px;
    flex: none;
  }
  .contact__address {
    margin: 4px 0 0;
    font-size: 12px;
    font-weight: 700;
    color: var(--brand-blue);
  }
  .swoosh {
    position: absolute;
    left: 0;
    bottom: 0;
    width: 501px;
    height: 80px;
  }
</style>
</head>
<body>
<main class="stage">
  <section class="card card--front" aria-label="Card front">
    <div class="wordmark"><span class="wordmark__dot"></span>Quillmark Ledger</div>
    <div class="website">www.quillmarkledger.example</div>
  </section>

  <section class="card card--back" aria-label="Card back">
    <div class="wordmark"><span class="wordmark__dot"></span>Quillmark Ledger</div>
    <div class="contact">
      <h1 class="contact__name">Dana Merrow</h1>
      <p class="contact__title">Founder/CEO</p>
      <ul class="contact__list">
        <li class="contact__item">
          <svg class="contact__icon" viewBox="0 0 20 20" aria-hidden="true">
            <circle cx="10" cy="10" r="10" fill="var(--brand-blue)"/>
            <path d="M5 8.5c0-1.5 2.2-2.5 5-2.5s5 1 5 2.5v1h-2.4v-1.3H7.4v1.3H5z" fill="#fff"/>
            <rect x="6" y="10" width="8" height="4.5" rx="1" fill="#fff"/>
          </svg>
          (617)555-0194
        </li>
        <li class="contact__item">
          <svg class="contact__icon" viewBox="0 0 20 20" aria-hidden="true">
            <circle cx="10" cy="10" r="10" fill="var(--brand-blue)"/>
            <rect x="5" y="6.5" width="10" height="7" fill="#fff"/>
            <path d="M5 6.5l5 4 5-4" fill="none" stroke="var(--brand-blue)" stroke-width="1"/>
          </svg>
          dana@quillmarkledger.example
        </li>
      </ul>
      <p class="contact__address">2740 Harlow Avenue, Boston MA 02135</p>
    </div>
    <svg class="swoosh" viewBox="0 0 501 80" preserveAspectRatio="none" aria-hidden="true">
      <path d="M110 70 C260 66 420 50 501 19 L501 31 C420 56 280 69 110 70 Z" fill="var(--brand-blue)"/>
      <path d="M0 67 C200 68 400 60 501 36 L501 80 L0 80 Z" fill="var(--brand-green)"/>
    </svg>
  </section>
</main>
</body>
</html>
```